Square Business Cards for Our Restaurant / Event Venue

We need square business cards designed for the management team of our event venue and restaurant. On one side of the card should be the the Harbor Lantern 7 logo and URL www.harborlantern7.example. On the other side should be the Ember Logo and URL www.emberhall7.example. All employee details should be on the side with Ember logo. There will be a total of 5 cards to be created with the design.

Clara Bennquist
clara@harborlantern7.example

main 555.418.3072
direct 555.730.2946

4831 West Orchard Lane SE
Washington, DC 90417

Industry/Entity Type

Business

```html
<!DOCTYPE html>
<html lang="en">
<head>
<meta charset="utf-8">
<title>Ember / Harbor Lantern 7 — Business Cards</title>
<link rel="stylesheet" href="https://fonts.googleapis.com/css2?family=PT+Sans:wght@400;700&family=PT+Sans+Narrow:wght@700&display=swap">
<style>
  :root {
    --backdrop: #9b9b9b;
    --ink-black: #0b0b0b;
    --paper: #dcdbdd;
    --brand-red: #8c171d;
    --accent-red: #b3252b;
    --text-light: #ececec;
  }
  * { margin: 0; padding: 0; box-sizing: border-box; }
  html, body {
    width: 1105px; height: 1200px; overflow: hidden;
    background: var(--backdrop);
    font-family: "PT Sans", sans-serif;
  }
  .sheet { position: relative; width: 1105px; height: 1200px; }
  .card {
    position: absolute; left: 175px; width: 755px; height: 428px; overflow: hidden;
  }
  .card--front { top: 118px; background: var(--ink-black); }
  .card--back { top: 636px; background: var(--brand-red); }

  .front-shape { position: absolute; inset: 0; }

  .contact { position: absolute; left: 30px; top: 76px; color: var(--text-light); }
  .contact__name {
    font-family: "PT Sans Narrow", sans-serif; font-weight: 700;
    font-size: 28px; line-height: 1; color: var(--accent-red); letter-spacing: 0.2px;
  }
  .contact__title { font-weight: 700; font-size: 19px; margin-top: 6px; letter-spacing: 0.3px; }
  .contact__address { font-size: 18.5px; line-height: 24px; margin-top: 20px; }
  .contact__list { list-style: none; margin-top: 14px; font-size: 18.5px; line-height: 24px; }
  .contact__list li { display: flex; align-items: center; gap: 9px; }
  .contact__list svg { width: 20px; height: 18px; flex: none; fill: var(--accent-red); }

  .ember-mark {
    position: absolute; left: 445px; top: 150px; width: 260px;
    display: flex; align-items: center; justify-content: center; gap: 12px;
  }
  .ember-mark__name {
    font-weight: 700; font-size: 86px; line-height: 1; color: var(--ink-black);
  }
  .ember-mark__dot { width: 18px; height: 18px; border-radius: 50%; background: var(--accent-red); }

  .venue-badge {
    position: absolute; left: 260px; top: 82px; width: 228px; height: 228px;
    border-radius: 50%; background: var(--paper);
    display: flex; align-items: center; justify-content: center; text-align: center;
  }
  .venue-badge__name {
    font-size: 30px; line-height: 1.1; color: var(--brand-red); font-weight: 400;
  }
  .venue-url {
    position: absolute; left: 0; right: 0; top: 356px; text-align: center;
    font-size: 17px; letter-spacing: 3.4px; color: var(--paper);
  }
</style>
</head>
<body>
<main class="sheet">
  <section class="card card--front" aria-label="Ember side">
    <svg class="front-shape" viewBox="0 0 755 428" width="755" height="428" aria-hidden="true">
      <path d="M582,0 C450,70 350,170 358,265 C365,345 440,400 525,428 L755,428 L755,0 Z" fill="var(--paper)"/>
      <path d="M500,30 C400,100 330,180 338,270 C345,350 420,400 490,428" fill="none" stroke="#f2f2f2" stroke-width="1.6"/>
    </svg>

    <div class="contact">
      <h1 class="contact__name">CLARA BENNQUIST</h1>
      <p class="contact__title">CEO/FOUNDER</p>
      <p class="contact__address">4831 West<br>Orchard Lane SE<br>Washington, DC 90417</p>
      <ul class="contact__list">
        <li><svg viewBox="0 0 20 18"><path d="M2 6c0-3 4-4 8-4s8 1 8 4v2h-4V6H6v2H2zM5 9h10l3 7H2z"/></svg>555.418.3072</li>
        <li><svg viewBox="0 0 20 18"><path d="M2 6c0-3 4-4 8-4s8 1 8 4v2h-4V6H6v2H2zM5 9h10l3 7H2z"/></svg>555.730.2946</li>
        <li><svg viewBox="0 0 20 18"><path d="M1 4h18v1l-9 6-9-6zM1 7l9 6 9-6v8H1z"/></svg>clara@harborlantern7.example</li>
        <li><svg viewBox="0 0 20 18"><circle cx="10" cy="10" r="8"/></svg>www.emberhall7.example</li>
      </ul>
    </div>

    <div class="ember-mark">
      <span class="ember-mark__name">Ember</span>
      <span class="ember-mark__dot"></span>
    </div>
  </section>

  <section class="card card--back" aria-label="Harbor Lantern 7 side">
    <div class="venue-badge">
      <span class="venue-badge__name">Harbor<br>Lantern 7</span>
    </div>
    <p class="venue-url">www.harborlantern7.example</p>
  </section>
</main>
</body>
</html>
```